We need visit card and a letter paper for our website. thx

We have a beauty clinic in Switzerland.
https://wolkenbachtal.ch
We need a visit card.

Requirements
Must have
• see colors on website

```html
<!DOCTYPE html>
<html lang="en">
<head>
<meta charset="utf-8">
<title>Wolkenbachtal – Business Card</title>
<link rel="stylesheet" href="https://fonts.googleapis.com/css2?family=Roboto:wght@400;500&display=swap">
<style>
  :root {
    --backdrop: #5b5b5d;
    --card: #2f2f31;
    --card-emboss: #3a3a3c;
    --accent: #d1457a;
    --ink: #ffffff;
  }
  * { margin: 0; padding: 0; box-sizing: border-box; }
  html, body {
    width: 1200px; height: 1125px; overflow: hidden;
    background: var(--backdrop);
    font-family: "Roboto", Arial, sans-serif;
  }
  .canvas {
    position: relative; width: 1200px; height: 1125px;
  }
  .card {
    position: absolute; left: 220px;
    width: 760px; height: 468px;
    background: var(--card);
    border-bottom: 9px solid var(--accent);
  }
  .card--back { top: 60px; }
  .card--front { top: 597px; }

  .card-back__name {
    position: absolute; inset: 0;
    display: flex; align-items: center; justify-content: center;
    font-size: 64px; font-weight: 400; color: var(--card-emboss);
    letter-spacing: 1px;
  }

  .brand {
    position: absolute; left: 40px; top: 0; width: 300px; height: 100%;
    display: flex; align-items: center; justify-content: center;
    font-size: 44px; font-weight: 400; color: var(--ink);
  }
  .divider {
    position: absolute; left: 372px; top: 130px;
    width: 2px; height: 210px; background: var(--accent);
  }
  .details {
    position: absolute; left: 398px; top: 128px;
    color: var(--ink);
  }
  .details__names {
    color: var(--accent); font-weight: 500; font-size: 25px; line-height: 32px;
    margin-bottom: 14px;
  }
  .details__address { font-size: 20px; line-height: 27px; margin-bottom: 18px; }
  .contact { list-style: none; font-size: 20px; line-height: 27px; }
  .contact li { display: flex; align-items: center; gap: 8px; }
  .contact svg { width: 16px; height: 16px; fill: var(--accent); flex: none; }
</style>
</head>
<body>
<main class="canvas">
  <section class="card card--back" aria-label="Card back">
    <div class="card-back__name">Wolkenbachtal</div>
  </section>

  <section class="card card--front" aria-label="Card front">
    <div class="brand">Wolkenbachtal</div>
    <div class="divider"></div>
    <div class="details">
      <p class="details__names">Dr. Lena Aebischer<br>Dr. Marco Steinlin, DESA</p>
      <p class="details__address">Lindenweg 7<br>7482 Bergün, Switzerland</p>
      <ul class="contact">
        <li>
          <svg viewBox="0 0 16 16" aria-hidden="true"><path d="M3.5 1.5l2.5 0 1 3.5-1.6 1.2c.8 1.8 2.2 3.2 4 4l1.2-1.6 3.4 1v2.6c0 .9-.8 1.6-1.7 1.5C6.8 13.2 2.8 9.2 2 3.7 1.9 2.5 2.6 1.5 3.5 1.5z"/></svg>
          +41 (0) 800 24 36 48
        </li>
        <li>
          <svg viewBox="0 0 16 16" aria-hidden="true"><path d="M1 3.5h14v1L8 9 1 4.5z"/><path d="M1 6l7 4.5L15 6v6.5H1z"/></svg>
          hallo@wolkenbachtal.ch
        </li>
        <li>
          <svg viewBox="0 0 16 16" aria-hidden="true"><circle cx="8" cy="8" r="7"/><path d="M4 5c1.5 0 2 1 3 1s1 1.5 0 2-1 2-2 2.5V9C4 8 3.5 6.5 4 5zM10 10c1-.5 2 0 2.5 1" fill="none" stroke="#2f2f31" stroke-width="1.2"/></svg>
          wolkenbachtal.ch
        </li>
      </ul>
    </div>
  </section>
</main>
</body>
</html>
```